DL FLYER - Stroll Sip Nibble Outings

I need a2-sided DL flyer designed to put into Hotel foyers. This will need to stand out as it will be in a rack with multiple other options.

Our tours are all about walking with us to take in great venues for food and beverages with art and history along the way.

We operate in Perth City plus Fremantle.

I am hoping for the flyer to look something like my website - https://strollsipnibble.example.au/

This website will be updated in the coming weeks with new experiences and a new booking platform.

I want the flyers to be used to drive bookings from the updated website.

Attached are several images that could be used also.

Target Market(s)

Social groups, couples, friends groups & foodies!

Industry/Entity Type

Food & Beverage Walking Tours

Font styles to use
Serif
Sans Serif
Decorative
Script

Colors
0094D4
00A9DD
6FCCEA
C7EBF8
E9F6FB
59FF00
82FF00
B8FF75
E3FFCB
F4FFEA
FFF300
FFF600
FEFA6F
FFFEC7
FFFEE8
F0912C
F2A743
F7CA91
FBE8D2
FDF5EE

Requirements
Must have
• Logo and must look fun. Discount code - CITYLOVESU for online price 15% off (not valid on gift voucher purchases)
Nice to have
• similar to my website - colours and styling. I will be updating available tours, costs and timing in the coming weeks. Check out my new booking link to get pricing and tour details - https://www-902k.tixlane.example/tixlane/b_strollsipnibbleoutings_start.html?ctlsrc2=Qm518LMNAB3JKty7GhqwZr4xcV%2F9P8ArbdwHn%2FUsPw%3D&src=07k
Should not have
• .

```html
<!DOCTYPE html>
<html lang="en">
<head>
<meta charset="utf-8">
<title>Stroll Sip Nibble Outings – DL Flyer</title>
<link rel="stylesheet" href="https://fonts.googleapis.com/css2?family=Fredoka:wght@500;600;700&family=Montserrat:wght@500;600;700;800&family=Oswald:wght@600&display=swap">
<style>
:root{
  --stage:#e9e9e9;
  --ink:#243737;
  --charcoal:#262626;
  --green:#6aa878;
  --green-soft:#93cba0;
  --orange:#ff6a13;
  --orange-soft:#f79a5c;
  --white:#ffffff;
}
*{box-sizing:border-box;margin:0;padding:0}
html,body{width:800px;height:1200px;overflow:hidden;background:var(--stage)}
.canvas{position:relative;width:800px;height:1200px}
.flyer{position:absolute;top:206px;width:350px;height:787px;overflow:hidden;font-family:"Montserrat",sans-serif;color:var(--ink)}
.flyer--front{left:35px;background:linear-gradient(180deg,#f1ebdb 0%,#e9e0cb 50%,#efe8d6 100%)}
.flyer--back{left:415px;background:linear-gradient(180deg,#f7cfc1 0%,#f4b9a6 45%,#f7c9ba 75%,#f8d6ca 100%)}
.backdrop{position:absolute;inset:0;width:100%;height:100%}

/* brand */
.brand{position:absolute;top:44px;left:0;width:100%;display:flex;justify-content:center;align-items:center;gap:8px}
.brand__dot{width:22px;height:22px;border-radius:50%;background:var(--orange)}
.brand__name{font-family:"Fredoka",sans-serif;font-weight:600;font-size:19px;color:var(--ink)}

.headline{position:absolute;top:104px;left:0;width:100%;text-align:center;font-family:"Fredoka",sans-serif;font-weight:700;line-height:1}
.headline__top{display:block;font-size:33px;color:var(--ink);letter-spacing:.2px}
.headline__bottom{display:block;font-size:54px;color:var(--green);margin-top:4px;letter-spacing:1px}

.hero-photo{position:absolute;left:60px;top:238px;width:236px;height:236px;border-radius:50%;
  background:radial-gradient(circle at 45% 55%,#f6a56a 0%,#e4773d 35%,#9a5a2c 65%,#3b2a1f 100%)}

.intro{position:absolute;top:496px;left:32px;width:286px;text-align:center;font-size:14.2px;font-weight:500;line-height:17.5px;color:#222}
.divider{position:absolute;top:580px;left:43px;width:266px;height:1px;background:#bdbdbd}
.divider::after{content:"";position:absolute;left:116px;top:-2px;width:34px;height:4px;border-radius:2px;background:var(--orange)}

.features{position:absolute;top:623px;left:25px;width:301px;height:77px;border:1.5px solid var(--orange-soft);border-radius:10px;display:flex}
.feature{flex:1;position:relative;text-align:center;padding-top:28px;font-family:"Fredoka",sans-serif;font-weight:600;font-size:12px;line-height:14px;color:var(--ink)}
.feature + .feature{border-left:1px solid #d8d8d8}
.feature__icon{position:absolute;top:-22px;left:50%;margin-left:-22px;width:44px;height:44px;border-radius:50%;background:var(--green-soft);border:1.5px solid var(--orange);display:flex;align-items:center;justify-content:center}

/* footer shared */
.footer-band{position:absolute;left:0;bottom:0;width:100%;height:64px;background:var(--ink)}
.phone{position:absolute;top:710px;left:56px;width:236px;height:31px;border-radius:16px;background:var(--orange);display:flex;align-items:center;padding-left:5px;gap:6px}
.phone__icon{width:23px;height:23px;border-radius:50%;background:var(--white);display:flex;align-items:center;justify-content:center}
.phone__number{font-family:"Oswald",sans-serif;font-weight:600;font-size:22px;color:var(--white);letter-spacing:.5px;line-height:1}
.website{position:absolute;top:748px;left:0;width:100%;text-align:center;font-family:"Montserrat",sans-serif;font-weight:700;font-size:12.5px;letter-spacing:1px;color:var(--white)}

/* back */
.section-title{position:absolute;top:28px;left:0;width:100%;text-align:center;font-family:"Fredoka",sans-serif;font-weight:700;font-size:21px;color:var(--charcoal)}
.section-title__mark{background:linear-gradient(180deg,transparent 20%,var(--green-soft) 20%,var(--green-soft) 90%,transparent 90%);border-radius:8px;padding:0 3px}

.tour{position:absolute;width:139px;height:157px}
.tour__head{height:28px;background:var(--charcoal);border-radius:12px 12px 0 0;color:var(--white);font-family:"Fredoka",sans-serif;font-weight:600;font-size:9.6px;line-height:10.4px;text-align:center;display:flex;align-items:center;justify-content:center;text-transform:uppercase;padding:0 8px}
.tour__head--mixed{text-transform:none}
.tour__body{position:relative;height:129px;background:var(--white);border:1px solid var(--charcoal);border-top:none;border-radius:0 0 12px 12px;text-align:center}
.tour__price{position:absolute;top:2px;left:0;width:100%;font-family:"Fredoka",sans-serif;font-weight:700;font-size:26px;line-height:30px;color:var(--orange)}
.tour__time{position:absolute;top:32px;left:0;width:100%;font-family:"Fredoka",sans-serif;font-weight:600;font-size:10.5px;color:var(--charcoal)}
.tour__place{position:absolute;top:47px;left:35px;width:69px;height:13px;border-radius:7px 7px 0 0;background:var(--orange);color:var(--white);font-weight:700;font-size:8.5px;line-height:13px}
.tour__photo{position:absolute;top:60px;left:14px;width:109px;height:64px;border:2px solid var(--white);border-radius:9px;box-shadow:0 0 0 1px #ddd}
.col-a{left:30px}.col-b{left:180px}
.row-1{top:67px}.row-2{top:237px}.row-3{top:407px}

.offer-lead{position:absolute;top:614px;left:0;width:100%;text-align:center;font-family:"Fredoka",sans-serif;font-weight:600;font-size:16px;color:var(--charcoal)}
.offer-lead__accent{color:var(--green)}
.offer-number{position:absolute;top:634px;left:56px;font-family:"Fredoka",sans-serif;font-weight:700;font-size:62px;line-height:62px;color:var(--orange);letter-spacing:-2px}
.offer-sign{position:absolute;top:636px;left:126px;font-family:"Fredoka",sans-serif;font-weight:700;font-size:34px;line-height:34px;color:var(--orange)}
.offer-off{position:absolute;top:672px;left:124px;font-family:"Fredoka",sans-serif;font-weight:600;font-size:18px;line-height:20px;color:var(--charcoal)}
.offer-rule{position:absolute;top:640px;left:180px;height:55px;border-left:1px dashed #555}
.offer-code{position:absolute;top:638px;left:189px}
.offer-code__label{font-family:"Fredoka",sans-serif;font-weight:600;font-size:12px;color:var(--orange)}
.offer-code__value{display:inline-block;margin-top:3px;font-family:"Montserrat",sans-serif;font-weight:800;font-size:15.5px;color:var(--charcoal);background:linear-gradient(180deg,transparent 25%,var(--green-soft) 25%);border-radius:6px;padding:0 2px}
.offer-code__note{margin-top:3px;font-size:7px;line-height:8px;font-weight:500;color:#333;width:110px}
</style>
</head>
<body>
<main class="canvas">

  <section class="flyer flyer--front">
    <svg class="backdrop" viewBox="0 0 350 787" aria-hidden="true">
      <circle cx="178" cy="345" r="132" fill="var(--orange-soft)"/>
      <path d="M0 400 Q60 470 140 482 Q178 488 216 482 Q290 470 350 400 L350 787 L0 787 Z" fill="var(--white)"/>
      <path d="M0 400 Q60 470 140 482 Q178 488 216 482 Q290 470 350 400" fill="none" stroke="var(--orange-soft)" stroke-width="6"/>
      <circle cx="178" cy="356" r="125" fill="var(--ink)"/>
    </svg>

    <div class="brand">
      <span class="brand__dot"></span>
      <span class="brand__name">Stroll Sip Nibble Outings</span>
    </div>

    <h1 class="headline">
      <span class="headline__top">Stroll Sip Nibble</span>
      <span class="headline__bottom">OUTINGS</span>
    </h1>

    <div class="hero-photo" role="img" aria-label="Friends clinking cocktail and beer glasses at a bar"></div>

    <p class="intro">Join us on foot as we hop between the best local spots for food and drinks, finding street art and old stories at every turn.</p>
    <div class="divider"></div>

    <div class="features">
      <div class="feature">
        <span class="feature__icon">
          <svg width="20" height="22" viewBox="0 0 20 22"><path d="M10 1a7 7 0 0 0-7 7c0 5 7 12 7 12s7-7 7-12a7 7 0 0 0-7-7z" fill="var(--orange)"/><circle cx="10" cy="8" r="2.6" fill="var(--green-soft)"/></svg>
        </span>
        Explore<br>The City
      </div>
      <div class="feature">
        <span class="feature__icon">
          <svg width="24" height="20" viewBox="0 0 24 20"><path d="M12 2C6 2 2 5.5 2 9.5c0 2.3 1.3 4.3 3.3 5.6L4 19l4.6-2.4c1.1.3 2.2.4 3.4.4 6 0 10-3.5 10-7.5S18 2 12 2z" fill="none" stroke="var(--orange)" stroke-width="2"/><circle cx="8" cy="9.5" r="1.5" fill="var(--orange)"/><circle cx="12" cy="9.5" r="1.5" fill="var(--orange)"/><circle cx="16" cy="9.5" r="1.5" fill="var(--orange)"/></svg>
        </span>
        Meet New<br>People
      </div>
      <div class="feature">
        <span class="feature__icon">
          <svg width="24" height="20" viewBox="0 0 24 20"><path d="M3 13h18a9 5 0 0 1-18 0z" fill="none" stroke="var(--orange)" stroke-width="1.8"/><path d="M2 13h20" stroke="var(--orange)" stroke-width="1.8"/><path d="M9 9c-1-1.5 1-2.5 0-4M12 9c-1-1.5 1-2.5 0-4M15 9c-1-1.5 1-2.5 0-4" fill="none" stroke="var(--orange)" stroke-width="1.4"/></svg>
        </span>
        Enjoy<br>Great Food
      </div>
    </div>

    <div class="footer-band"></div>
    <div class="phone">
      <span class="phone__icon"><svg width="13" height="13" viewBox="0 0 24 24"><path d="M6.6 10.8a15 15 0 0 0 6.6 6.6l2.2-2.2c.3-.3.7-.4 1-.2 1.1.4 2.3.6 3.6.6.6 0 1 .4 1 1V20c0 .6-.4 1-1 1A17 17 0 0 1 3 4c0-.6.4-1 1-1h3.5c.6 0 1 .4 1 1 0 1.3.2 2.5.6 3.6.1.3 0 .7-.2 1z" fill="var(--ink)"/></svg></span>
      <span class="phone__number">+61 400 123 456</span>
    </div>
    <p class="website">www.strollsipnibble.example.au</p>
  </section>

  <section class="flyer flyer--back">
    <svg class="backdrop" viewBox="0 0 350 787" aria-hidden="true">
      <path d="M0 605 Q170 555 350 592 L350 787 L0 787 Z" fill="var(--white)"/>
      <path d="M0 600 Q150 545 320 590 Q160 572 0 668 Z" fill="var(--green-soft)"/>
    </svg>

    <h2 class="section-title">TOURS &amp; <span class="section-title__mark">EXPERIENCES</span></h2>

    <article class="tour col-a row-1">
      <div class="tour__head">Steaks &amp;<br>Suds</div>
      <div class="tour__body">
        <div class="tour__price">$95</div>
        <div class="tour__time">1:30 PM - 5:00 PM</div>
        <div class="tour__place">Perth</div>
        <div class="tour__photo" role="img" aria-label="Plated dish with rice on a wooden table" style="background:linear-gradient(135deg,#5a3a26,#d7a26b 50%,#6b4a31)"></div>
      </div>
    </article>

    <article class="tour col-b row-1">
      <div class="tour__head">Golden hour<br>supper stroll</div>
      <div class="tour__body">
        <div class="tour__price">$99</div>
        <div class="tour__time">4:00 PM - 8:00 PM</div>
        <div class="tour__place">Perth</div>
        <div class="tour__photo" role="img" aria-label="Wine being poured into a glass beside an ice bucket" style="background:linear-gradient(135deg,#2b2b2e,#9a8f88 50%,#c96a55)"></div>
      </div>
    </article>

    <article class="tour col-a row-2">
      <div class="tour__head">Sunday sips by<br>the port</div>
      <div class="tour__body">
        <div class="tour__price">$99</div>
        <div class="tour__time">3:00 PM - 7:00</div>
        <div class="tour__place">Fremantle</div>
        <div class="tour__photo" role="img" aria-label="Guests laughing with drinks at a brick-walled venue" style="background:linear-gradient(135deg,#7a3227,#c98a6e 50%,#3c4a6a)"></div>
      </div>
    </article>

    <article class="tour col-b row-2">
      <div class="tour__head">Midweek<br>noodle nibbles</div>
      <div class="tour__body">
        <div class="tour__price">$75</div>
        <div class="tour__time">6:00 PM - 9:00 PM</div>
        <div class="tour__place">Fremantle</div>
        <div class="tour__photo" role="img" aria-label="Group sharing dishes at a busy restaurant table" style="background:linear-gradient(135deg,#e9e4df,#b98a6a 50%,#5d4a44)"></div>
      </div>
    </article>

    <article class="tour col-a row-3">
      <div class="tour__head tour__head--mixed">A Long Lunch<br>in Town</div>
      <div class="tour__body">
        <div class="tour__price">$90</div>
        <div class="tour__time">11:45 AM - 3:15 PM</div>
        <div class="tour__place">Perth</div>
        <div class="tour__photo" role="img" aria-label="Bowls of dumplings and salad on a table" style="background:linear-gradient(135deg,#d9d3c8,#c9a46e 50%,#8aa0a8)"></div>
      </div>
    </article>

    <article class="tour col-b row-3">
      <div class="tour__head">Cosy<br>winter sips</div>
      <div class="tour__body">
        <div class="tour__price">$95</div>
        <div class="tour__time">11:45 AM - 2:45 PM</div>
        <div class="tour__place">Perth</div>
        <div class="tour__photo" role="img" aria-label="Tour guide speaking to a group inside a cosy venue" style="background:linear-gradient(135deg,#4a2e28,#8a5a48 50%,#2a2a2a)"></div>
      </div>
    </article>

    <p class="offer-lead"><span class="offer-lead__accent">BOOK ONLINE</span> TO GET</p>
    <div class="offer-number">15</div>
    <div class="offer-sign">%</div>
    <div class="offer-off">OFF</div>
    <div class="offer-rule"></div>
    <div class="offer-code">
      <div class="offer-code__label">DISCOUNT CODE</div>
      <div class="offer-code__value">CITYLOVESU</div>
      <p class="offer-code__note">(not valid on gift voucher purchases)</p>
    </div>

    <div class="footer-band"></div>
    <div class="phone">
      <span class="phone__icon"><svg width="13" height="13" viewBox="0 0 24 24"><path d="M6.6 10.8a15 15 0 0 0 6.6 6.6l2.2-2.2c.3-.3.7-.4 1-.2 1.1.4 2.3.6 3.6.6.6 0 1 .4 1 1V20c0 .6-.4 1-1 1A17 17 0 0 1 3 4c0-.6.4-1 1-1h3.5c.6 0 1 .4 1 1 0 1.3.2 2.5.6 3.6.1.3 0 .7-.2 1z" fill="var(--ink)"/></svg></span>
      <span class="phone__number">+61 400 123 456</span>
    </div>
    <p class="website">www.strollsipnibble.example.au</p>
  </section>

</main>
</body>
</html>
```